Real Estate Open House A Frame Sign

The sign is 22" wide and 28" tall. This sign is used to post around the neighbourhood to direct people to an open house (home that is for sale). It is also used for self-promotion.

Designwise
- I just want something with a modern look, simple and clean.
- I want my picture and business logo on the left side.
- On the right side, website (www.brindle-realestate.com) and my phone (510-364-2918), then a blank space where I can write an address when I need to.

I'm not sure how I want the overall design look. I'm very open-minded and I'm depending on your creative mind to come up with something.

If you have any questions, please let me know.

```html
<!DOCTYPE html>
<html lang="en">
<head>
<meta charset="utf-8">
<title>Brindle Real Estate – Open House Sign</title>
<link href="https://fonts.googleapis.com/css2?family=Cinzel:wght@700&family=Josefin+Sans:wght@300&display=swap" rel="stylesheet">
<style>
  :root {
    --page-bg: #f2f3f5;
    --slate: #55565b;
    --navy: #003f7f;
    --white: #ffffff;
    --portrait-top: #6a6c72;
    --portrait-bottom: #2a2c33;
  }
  * { margin: 0; padding: 0; box-sizing: border-box; }
  html, body {
    width: 1129px;
    height: 1200px;
    overflow: hidden;
    background: var(--page-bg);
  }
  .sign {
    position: absolute;
    left: 124px;
    top: 40px;
    width: 880px;
    height: 1120px;
    border-radius: 22px;
    overflow: hidden;
    display: flex;
    box-shadow: 0 6px 24px rgba(0,0,0,0.18);
  }
  .agent-column {
    width: 360px;
    height: 100%;
    background: var(--slate);
    border-right: 5px solid var(--white);
    display: flex;
    flex-direction: column;
    align-items: center;
    padding-top: 90px;
  }
  .agent-portrait {
    width: 280px;
    height: 420px;
    border-radius: 140px 140px 0 0;
    background: linear-gradient(180deg, var(--portrait-top), var(--portrait-bottom));
    border-bottom: 5px solid var(--white);
  }
  .brand-name {
    margin-top: 90px;
    color: var(--white);
    font-family: "Josefin Sans", sans-serif;
    font-weight: 300;
    line-height: 1;
    text-align: center;
  }
  .brand-name .word {
    display: block;
    font-size: 58px;
    letter-spacing: 0.04em;
  }
  .brand-name .sub {
    display: block;
    margin-top: 16px;
    font-size: 22px;
    letter-spacing: 0.3em;
    padding-left: 0.3em;
  }
  .info-column {
    flex: 1;
    height: 100%;
    background: var(--navy);
    color: var(--white);
    font-family: "Cinzel", serif;
    font-weight: 700;
    text-align: center;
    display: flex;
    flex-direction: column;
    align-items: center;
    padding: 90px 50px 80px;
  }
  .sale-title {
    font-size: 88px;
    line-height: 1.12;
    letter-spacing: 0.28em;
    padding-left: 0.28em;
  }
  .contact {
    margin-top: 60px;
    line-height: 1.15;
  }
  .contact .phone {
    display: block;
    font-size: 46px;
    letter-spacing: 0.04em;
  }
  .contact .web {
    display: block;
    font-size: 22px;
    letter-spacing: 0.06em;
  }
  .address-space {
    margin-top: auto;
    width: 100%;
    height: 300px;
    border: 4px solid var(--white);
    border-radius: 12px;
  }
</style>
</head>
<body>
  <main class="sign">
    <aside class="agent-column">
      <div class="agent-portrait" role="img" aria-label="Portrait photo of the agent in a dark suit, arms crossed"></div>
      <div class="brand-name">
        <span class="word">BRINDLE</span>
        <span class="sub">REAL ESTATE</span>
      </div>
    </aside>
    <section class="info-column">
      <h1 class="sale-title">FOR<br>SALE</h1>
      <p class="contact">
        <span class="phone">510-364-2918</span>
        <span class="web">BRINDLE-REALESTATE.COM</span>
      </p>
      <div class="address-space" aria-label="Blank space for writing the property address"></div>
    </section>
  </main>
</body>
</html>
```